Eye catchy Construction Development business cards and stationery
Torvane Arch
Modern
Your Name
Managing Director
11111 My Street suite #100 City, STATE 66211
myemail@email.com
www.mywebsite.com
Use my winning logo from here http://www.plumvexstudio.com/contests/logo-for-construction-developer-company
Some elegant but modern design. One idea would be to use the company logo printed on silver metallic look, such as http://www.plumvexstudio.com/contests/theoakhearth-logo-project

```html
<!DOCTYPE html>
<html lang="en">
<head>
<meta charset="utf-8">
<title>Torvane Arch – Business Card</title>
<link rel="stylesheet" href="https://fonts.googleapis.com/css2?family=Oswald:wght@400;600&family=Special+Elite&display=swap">
<style>
  :root {
    --backdrop: #2b2c2e;
    --card-white: #ffffff;
    --brand-blue: #1e82b5;
    --brand-orange: #e9a23b;
    --ink-light: #ffffff;
  }
  * { margin: 0; padding: 0; box-sizing: border-box; }
  html, body {
    width: 1200px; height: 816px; overflow: hidden;
    background: var(--backdrop);
  }
  .canvas {
    width: 1200px; height: 816px;
    display: flex; align-items: center; justify-content: center;
  }
  .card {
    position: relative;
    width: 1000px; height: 572px;
    border-radius: 34px;
    background: var(--card-white);
    overflow: hidden;
  }
  .brand {
    position: absolute;
    left: 0; top: 0; width: 420px; height: 100%;
    display: flex; align-items: center; justify-content: center; gap: 14px;
    padding-top: 40px;
  }
  .brand-dot {
    width: 30px; height: 30px; border-radius: 50%;
    background: var(--brand-orange);
  }
  .brand-name {
    font-family: "Oswald", sans-serif;
    font-weight: 600;
    font-size: 46px;
    color: var(--brand-blue);
    letter-spacing: 0.5px;
  }
  .contact-panel {
    position: absolute;
    left: 406px; top: 0; width: 594px; height: 100%;
    background: var(--brand-blue);
    clip-path: polygon(14px 0, 100% 0, 100% 100%, 14px 100%, 14px 322px, 0 308px, 14px 294px);
    color: var(--ink-light);
  }
  .contact-list {
    list-style: none;
    position: absolute; left: 52px; top: 52px;
    font-family: "Special Elite", monospace;
    font-size: 21px; letter-spacing: 1px;
  }
  .contact-item {
    display: flex; align-items: flex-start; gap: 18px;
    margin-bottom: 26px;
  }
  .contact-item svg { flex: none; width: 20px; height: 20px; margin-top: 2px; }
  .contact-address { line-height: 1.35; }
  .person {
    position: absolute; right: 52px; top: 372px;
    text-align: right;
    font-family: "Oswald", sans-serif;
    text-transform: uppercase;
  }
  .person-name { font-size: 44px; font-weight: 600; letter-spacing: 1px; line-height: 1.1; }
  .person-title { font-size: 24px; font-weight: 400; letter-spacing: 1px; }
</style>
</head>
<body>
<main class="canvas">
  <section class="card">
    <div class="brand">
      <span class="brand-dot"></span>
      <span class="brand-name">Torvane Arch</span>
    </div>
    <div class="contact-panel">
      <ul class="contact-list">
        <li class="contact-item">
          <svg viewBox="0 0 20 20" aria-hidden="true"><path fill="#fff" d="M5 2l3 4-2 2c1 2 3 4 5 5l2-2 4 3-2 3C9 17 3 11 2 4z"/></svg>
          <span>+2 (014) 57-480-16</span>
        </li>
        <li class="contact-item">
          <svg viewBox="0 0 20 20" aria-hidden="true"><rect x="2" y="4" width="16" height="12" rx="1" fill="#fff"/><path d="M2 5l8 6 8-6" stroke="#1e82b5" stroke-width="1.6" fill="none"/></svg>
          <span>info@torvanearch.com</span>
        </li>
        <li class="contact-item">
          <svg viewBox="0 0 20 20" aria-hidden="true"><circle cx="10" cy="10" r="8" fill="#fff"/></svg>
          <span>www.torvanearch.com</span>
        </li>
        <li class="contact-item">
          <svg viewBox="0 0 20 20" aria-hidden="true"><path fill="#fff" d="M10 2l8 7h-2v8h-4v-5H8v5H4V9H2z"/></svg>
          <span class="contact-address">418 Corbel Lane,<br>NE Harwick, USA</span>
        </li>
      </ul>
      <div class="person">
        <p class="person-name">Dalen Forsby</p>
        <p class="person-title">General Manager</p>
      </div>
    </div>
  </section>
</main>
</body>
</html>
```